Tall Maple Hydration Product that supports healthy blood pressure and Hydration

Design Brief: Hydration Product for Blood Pressure Support
Product Name: "42" or "Brisk"
We are developing a hydration product aimed at supporting healthy blood pressure while keeping users hydrated. The product will have a clinical, clean, and functional design, and we're looking for a professional designer or team to bring this vision to life.

Project Overview
We want a product design (logo, label, and possibly packaging) that communicates:

Hydration

Blood pressure support

Pharmaceutical/medical Look

Health and wellness

This product will be used by health-conscious consumers and individuals managing their blood pressure.

Design Objectives
Reflect both hydration and blood pressure support visually.

Appeal to a clinical, trustworthy, yet fresh and modern aesthetic.

Clearly communicate functionality and health benefits.

Visual Elements to Consider
We would like to explore the use of the following visual motifs:

Water drop – to symbolize hydration

Blood drop – to signify blood pressure support

Medical or pharmaceutical elements – cross, heartbeat/EKG lines, capsules, etc.

Typography – Clean, sans-serif fonts; professional and modern

Color Preferences
We have attached reference images showing preferred color schemes. These are mostly in the blue, red, and white family (for hydration, blood, and clinical cleanliness).

However, we are open to other colors that you feel will enhance the brand’s purpose.

Target Market(s)

Hydration

Industry/Entity Type

Health and Wellness

Font styles to use
Serif
Sans Serif
Decorative
Script

Colors
00AB8E
00BBA5
67D7C9
C6EFE9
E9F9F6

Requirements
Must have
• design that incorporates a clean pharmaceutical look and refreshing design
Nice to have
• Medica look
Should not have
• Clean Design. Silver and Cobalt Blue Design as an additional

```html
<!DOCTYPE html>
<html lang="en">
<head>
<meta charset="utf-8">
<title>Tall Maple — 42 Daily Hydration</title>
<link href="https://fonts.googleapis.com/css2?family=Jost:wght@300;400;500;600&display=swap" rel="stylesheet">
<style>
  :root {
    --brand-blue: #2f4b9c;
    --label-blue: #3f4a9e;
    --label-blue-deep: #262f7e;
    --sachet-blue: #223189;
    --sachet-deep: #1a2370;
    --number-grey: #9c9ca4;
    --fresh-green: #3dbd86;
    --white: #ffffff;
    --band-white: #eef0f4;
    --band-teal: #4fc9bd;
    --band-orange: #eb9b68;
    --band-yellow: #f1cc7c;
    --page: #f7f7f8;
  }
  * { margin: 0; padding: 0; box-sizing: border-box; }
  html, body { width: 1200px; height: 876px; overflow: hidden; }
  body {
    background: var(--page);
    font-family: "Jost", sans-serif;
    position: relative;
  }

  /* Brand name */
  .brand-name {
    position: absolute; left: 616px; top: 252px;
    font-weight: 500; font-size: 82px; line-height: 1;
    color: var(--brand-blue); letter-spacing: 1px; white-space: nowrap;
  }

  /* Shared product type */
  .product-number {
    position: absolute; font-weight: 300; color: var(--number-grey);
    line-height: 1; white-space: nowrap;
  }
  .title-daily, .title-hydration, .subtitle {
    position: absolute; line-height: 1; white-space: nowrap;
  }
  .title-daily, .title-hydration { font-weight: 500; color: var(--fresh-green); }
  .subtitle { color: var(--white); font-weight: 400; }
  .colour-band {
    position: absolute; left: 0; bottom: 0;
    background: linear-gradient(180deg,
      var(--band-white) 0%, var(--band-teal) 38%,
      var(--band-orange) 68%, var(--band-yellow) 100%);
  }

  /* Bottle label, flat */
  .label {
    position: absolute; left: 120px; top: 250px;
    width: 320px; height: 340px; overflow: hidden;
    background: linear-gradient(90deg, var(--label-blue-deep) 0%, var(--label-blue) 45%, #4f5aab 100%);
  }
  .label-brand {
    position: absolute; right: 26px; top: 62px;
    color: var(--white); font-weight: 500; font-size: 22px; letter-spacing: .5px;
    line-height: 1; white-space: nowrap;
  }
  .label .product-number { left: 10px; top: 100px; font-size: 108px; letter-spacing: -6px; }
  .label .title-daily { left: 136px; top: 120px; font-size: 36px; }
  .label .title-hydration { left: 136px; top: 156px; font-size: 28px; letter-spacing: .3px; }
  .label .subtitle { left: 136px; top: 188px; font-size: 16px; }
  .label .colour-band { width: 320px; height: 100px; }

  /* Sachet, flat */
  .sachet {
    position: absolute; left: 500px; top: 600px;
    width: 500px; height: 146px; overflow: hidden;
    background: linear-gradient(90deg, var(--sachet-blue) 0%, #2a3a94 30%, var(--sachet-deep) 100%);
  }
  .sachet-seal {
    position: absolute; left: 0; top: 0; width: 62px; height: 100%;
    border-right: 2px solid rgba(0,0,0,.25);
  }
  .sachet-hole {
    position: absolute; left: 16px; top: 66px; width: 14px; height: 10px;
    border-radius: 50%; background: var(--page);
  }
  .sachet-brand {
    position: absolute; left: 131px; top: 66px;
    transform: translate(-50%, -50%) rotate(-90deg);
    white-space: nowrap; line-height: 1;
    color: var(--white); font-weight: 500; font-size: 17px;
  }
  .sachet .product-number { left: 204px; top: 14px; font-size: 72px; letter-spacing: -4px; }
  .sachet .title-daily { left: 292px; top: 20px; font-size: 24px; }
  .sachet .title-hydration { left: 292px; top: 45px; font-size: 18px; letter-spacing: .3px; }
  .sachet .subtitle { left: 292px; top: 66px; font-size: 12px; }
  .sachet .colour-band { left: 196px; width: 304px; height: 50px; }
</style>
</head>
<body>

  <div class="brand-name">TALL MAPLE</div>

  <section class="label">
    <div class="label-brand">TALL MAPLE</div>
    <div class="product-number">42</div>
    <div class="title-daily">DAILY</div>
    <div class="title-hydration">HYDRATION</div>
    <div class="subtitle">Electrolytes Powder</div>
    <div class="colour-band" role="img" aria-label="Layered wave pattern in white, teal, orange and yellow"></div>
  </section>

  <section class="sachet">
    <div class="sachet-seal"><span class="sachet-hole"></span></div>
    <div class="sachet-brand">TALL MAPLE</div>
    <div class="product-number">42</div>
    <div class="title-daily">DAILY</div>
    <div class="title-hydration">HYDRATION</div>
    <div class="subtitle">Electrolytes Powder</div>
    <div class="colour-band" role="img" aria-label="Layered wave pattern in white, teal, orange and yellow"></div>
  </section>

</body>
</html>
```